Lanternway 7.5 - Educational Guide/Course-pack/Worksheet

Our Lanternway 7.5 toolkit is an educational workshop that focuses on inspiring student initiatives in the classroom! We need a new educational course guide or course-pack for students/teachers that clearly outlines or explains the program steps, offers helpful tips and includes empty spaces/lines where their can write down their great ideas or notes. This will include a;

- Teachers Guide (1 Page)
- Student Guide/Worksheet (4 Pages)
- Group Pack Resources (3 Pages)

This will consist of designing/formatting text, stock animation/icons, font, etc. We have included our new logo (color, branding, etc.) and all of the text for each separate course-pack. We have also attached our new website to give you an idea of the program style.

Our workshop can be for any school project like Technology, Community, Environment, Art, Science, etc.

Target Market(s)

High School Students/Teachers

Industry/Entity Type

Education

Font styles to use
Sans Serif

Colors
f68e4e
acd037
34a7d8

Requirements
Must have
• Use our brand colors from logo.
Should not have
• Should not be too childish.

```html
<!DOCTYPE html>
<html lang="en">
<head>
<meta charset="utf-8">
<title>Lanternway 7.5 – Teacher's Guide: The Big Pitch &amp; Launch</title>
<link href="https://fonts.googleapis.com/css2?family=Raleway:wght@400;600;700;800&display=swap" rel="stylesheet">
<style>
  :root {
    --blue: #159dc4;
    --orange: #f7a021;
    --green: #a6ce39;
    --ink: #1f1f1f;
    --grey: #6d6e71;
    --rule: #7a7a7a;
    --paper: #ffffff;
  }
  * { box-sizing: border-box; margin: 0; padding: 0; }
  html, body { width: 849px; height: 1200px; overflow: hidden; }
  body {
    position: relative;
    background: var(--paper);
    font-family: "Raleway", Arial, sans-serif;
    color: var(--ink);
    font-size: 11.6px;
    line-height: 15.7px;
  }
  .brand-band { position: absolute; top: 0; left: 0; width: 849px; height: 15px; display: flex; }
  .brand-band span:nth-child(1) { width: 576px; background: var(--blue); }
  .brand-band span:nth-child(2) { width: 142px; background: var(--orange); }
  .brand-band span:nth-child(3) { flex: 1; background: var(--green); }

  .step-icon {
    position: absolute; width: 112px; height: 112px; border-radius: 50%;
    background: var(--blue);
  }
  .step-title {
    position: absolute; left: 263px;
    font-size: 19px; line-height: 22px; font-weight: 800; color: var(--blue);
  }
  .step-rule {
    position: absolute; left: 157px; width: 607px; height: 1px; background: var(--rule);
  }
  .step-rule::after {
    content: ""; position: absolute; right: -5px; top: -5px;
    width: 10px; height: 10px; border-radius: 50%; background: var(--blue);
  }
  .duration {
    position: absolute; left: 172px; font-weight: 700; font-size: 12px;
    display: flex; align-items: center; gap: 4px;
  }
  .duration svg { width: 13px; height: 13px; }
  .duration.plain { left: 190px; line-height: 15.7px; }
  .block { position: absolute; left: 263px; width: 520px; }
  .block h3 { font-size: 12px; font-weight: 700; line-height: 15.7px; }
  .block p { font-weight: 400; }
  .block strong { font-weight: 700; }
  .objectives { list-style: none; margin-top: 1px; }
  .objectives li { position: relative; padding-left: 17px; line-height: 17.2px; }
  .objectives li::before {
    content: ""; position: absolute; left: 1px; top: 4px;
    width: 6px; height: 6px; background: var(--orange);
  }
  .gap { height: 15.7px; }

  .tip-tick { position: absolute; left: 134px; width: 42px; height: 42px; }
  .tip { position: absolute; left: 190px; width: 600px; }
  .tip h4 { font-size: 12px; font-weight: 700; }

  .footer-rule { position: absolute; left: 83px; top: 1040px; width: 693px; height: 1px; background: var(--rule); }
  .footer-divider { position: absolute; left: 362px; top: 1063px; width: 1px; height: 97px; background: var(--rule); }
  .sponsors { position: absolute; left: 380px; top: 1064px; font-size: 11.6px; color: var(--ink); letter-spacing: 0.3px; }
  .brand-lockup { position: absolute; left: 86px; top: 1068px; display: flex; align-items: center; gap: 12px; }
  .brand-lockup .dot { width: 52px; height: 52px; border-radius: 50%; background: var(--blue); }
  .brand-lockup .name { font-size: 28px; font-weight: 700; color: var(--grey); letter-spacing: -0.3px; }
  .powered { position: absolute; left: 157px; top: 1140px; font-size: 11.6px; }
</style>
</head>
<body>
  <div class="brand-band"><span></span><span></span><span></span></div>

  <!-- Step 4 -->
  <div class="step-icon" style="left:51px; top:76px;" role="img" aria-label="Megaphone held in hand icon"></div>
  <h2 class="step-title" style="top:76px;">4.&nbsp; The Big Pitch</h2>
  <div class="step-rule" style="top:106px;"></div>

  <div class="duration" style="top:114px;">
    <svg viewBox="0 0 14 14" fill="none" stroke="#159dc4" stroke-width="1.2"><circle cx="7" cy="8" r="5"/><path d="M7 5.5V8l1.6 1.2M2 3.2 4 1.6M12 3.2 10 1.6"/></svg>5 min
  </div>
  <div class="block" style="top:113px;">
    <h3>Prepare</h3>
    <p>Participants list the positive points and challenges regarding the project.</p>
    <div class="gap"></div>
    <h3>Objectives</h3>
    <ul class="objectives">
      <li>Identify potential selling points and to strengthen project-development skills</li>
      <li>Recognize the value of a project and increase appreciation and attachment to it</li>
    </ul>
  </div>

  <div class="duration plain" style="top:226px;">4-5 min<br>per group</div>
  <div class="block" style="top:226px; width:540px;">
    <h3>Present</h3>
    <p>Participants present and defend their project idea to the other groups.</p>
    <p>Members from other groups ask questions to clarify and critique each presentation</p>
    <p><strong>Teacher animates the exchange to keep order and keep questions/comments flowing.</strong></p>
    <div class="gap"></div>
    <h3>Objectives</h3>
    <ul class="objectives">
      <li>Improve presentation skills</li>
      <li>Fine-tune project planning by collecting more opinions and observations</li>
    </ul>
  </div>

  <!-- Step 5 -->
  <div class="step-icon" style="left:51px; top:362px;" role="img" aria-label="Rocket launching icon"></div>
  <h2 class="step-title" style="top:380px;">5.&nbsp; Launch Your Project!</h2>
  <div class="step-rule" style="top:406px;"></div>

  <div class="duration" style="top:417px;">
    <svg viewBox="0 0 14 14" fill="none" stroke="#159dc4" stroke-width="1.2"><circle cx="7" cy="8" r="5"/><path d="M7 5.5V8l1.6 1.2M2 3.2 4 1.6M12 3.2 10 1.6"/></svg>10 min
  </div>
  <div class="block" style="top:416px;">
    <h3>The Who’s Who?</h3>
    <p>Participants match each group member with a profile description to determine which position or committee is best for each member.</p>
    <div class="gap"></div>
    <h3>Objectives:</h3>
    <ul class="objectives">
      <li>Discover traits and talents as perceived by one’s self and by one’s peers.</li>
      <li>Learn that each member’s abilities are valuable in the realization of any project.</li>
      <li>Validate and highlight characteristics that are often taken for granted.</li>
    </ul>
    <div class="gap"></div>
    <h3>The G-Pack!</h3>
    <p>Distribute one G-Pack to each group.</p>
    <p>These optional tools will help students autonomously plan and implement their project.</p>
    <div class="gap"></div>
    <h3>Objective:</h3>
    <ul class="objectives">
      <li>Set the scene for participants to take responsibility for their project.</li>
    </ul>
  </div>

  <!-- Tips -->
  <svg class="tip-tick" style="top:672px;" viewBox="0 0 42 42"><circle cx="21" cy="21" r="19.5" fill="none" stroke="#159dc4" stroke-width="1.5"/><path d="M12 21l6 6 12-12" fill="none" stroke="#f7a021" stroke-width="4" stroke-linecap="round" stroke-linejoin="round"/></svg>
  <div class="tip" style="top:673px;">
    <h4>The Launch Continues</h4>
    <p>The implementation of the projects is an ongoing process.</p>
    <p>The teacher’s role is to provide continued support and motivation.</p>
  </div>

  <svg class="tip-tick" style="top:740px;" viewBox="0 0 42 42"><circle cx="21" cy="21" r="19.5" fill="none" stroke="#159dc4" stroke-width="1.5"/><path d="M12 21l6 6 12-12" fill="none" stroke="#f7a021" stroke-width="4" stroke-linecap="round" stroke-linejoin="round"/></svg>
  <div class="tip" style="top:736px;">
    <h4>Timeline</h4>
    <p>Tell the participants how much time they have to accomplish their project.</p>
    <p>Do the projects have to take place during a particular time period or event or by a certain deadline?</p>
  </div>

  <svg class="tip-tick" style="top:801px;" viewBox="0 0 42 42"><circle cx="21" cy="21" r="19.5" fill="none" stroke="#159dc4" stroke-width="1.5"/><path d="M12 21l6 6 12-12" fill="none" stroke="#f7a021" stroke-width="4" stroke-linecap="round" stroke-linejoin="round"/></svg>
  <div class="tip" style="top:798px;">
    <h4>Frequency</h4>
    <p>Tell participants when they will be able to work on the project in class.</p>
    <p>Ex.&nbsp; The first 30 minutes of each period, one class per week, every class for a few weeks, etc.</p>
  </div>

  <svg class="tip-tick" style="top:867px;" viewBox="0 0 42 42"><circle cx="21" cy="21" r="19.5" fill="none" stroke="#159dc4" stroke-width="1.5"/><path d="M12 21l6 6 12-12" fill="none" stroke="#f7a021" stroke-width="4" stroke-linecap="round" stroke-linejoin="round"/></svg>
  <div class="tip" style="top:861px;">
    <h4>Updates</h4>
    <p>Get progress reports from the project managers (Chameleons).</p>
    <p>Remind them that their job is to motivate their team and keep track of what people are doing They should not be “doing everything”.</p>
  </div>

  <svg class="tip-tick" style="top:940px;" viewBox="0 0 42 42"><circle cx="21" cy="21" r="19.5" fill="none" stroke="#159dc4" stroke-width="1.5"/><path d="M12 21l6 6 12-12" fill="none" stroke="#f7a021" stroke-width="4" stroke-linecap="round" stroke-linejoin="round"/></svg>
  <div class="tip" style="top:939px;">
    <h4>The Goal</h4>
    <p>In times of difficulty, remind them that their goal is to make something happen, even if it is not what they originally planned or had in mind.</p>
    <p>Our goal is to teach them to adapt their approaches and plans, and ultimately succeed.</p>
  </div>

  <!-- Footer -->
  <div class="footer-rule"></div>
  <div class="brand-lockup">
    <span class="dot"></span>
    <span class="name">Lanternway 7.5</span>
  </div>
  <p class="powered">Lanternway 7.5 is powered by:</p>
  <div class="footer-divider"></div>
  <p class="sponsors">SPONSOR LOGOS?</p>
</body>
</html>
```